Upstart Retirement Planning Firm needs help with business card design

Harborlight Wealth Partners, LLC is looking for help with business card design. We give advice on investments, insurance, and other financial matters related to retirement. There are some required disclosures that we will provide but mostly we are looking for a professional, classy business card that reflects the theme we have chosen. We have a logo that is attached but we would like to add a phrase; "Shaping Your Working Savings Into a Confident Retirement"

Doubled sided only so that we can add the required disclosures (needed for our industry) on the back of the card. We will provide the exact words for this in 1-2 days.

Target Market(s)

Retirees and Pre-retirees. Professionals 50+ years old

Industry/Entity Type

Financial Planning

Contact Information for Business Card

We currently have two people who will need separate cards so we'd like to have a template so that we can add names for new cards in the future.

For the first run, please show the following information.

Neil Osgood, MSF, CPA
Senior Wealth Advisor, Licensed Representative
nosgood@harborlightwp.example
Phone: (555) 218-3960
Toll Free Fax: (555) 218-3961

Address is
2876 Meadowbrook Pkwy.
Suite K418
Cedar Harbor, NC 23019

Colors
3277b5

Requirements
Must have
• Logo, contact info, small phase to describe business (in description), required legal disclosures on back of the card as follows (in small font)
• Neil Osgood is a registered representative of and offers securities through Brightwater Capital Brokerage Corporation, Member SIPC. Brightwater Capital Brokerage Corporation is a member of the Brightwater Advisory Group which is the marketing name for Brightwater Holding Corporation and its affiliates.
Nice to have
• Rounded edges, raised letters
Should not have
• any colors that aren't in the logo (other than black for font)

```html
<!DOCTYPE html>
<html lang="en">
<head>
<meta charset="utf-8">
<title>Harborlight Wealth Partners – Business Card</title>
<link rel="stylesheet" href="https://fonts.googleapis.com/css2?family=Arimo:wght@400&family=Marcellus+SC&display=swap">
<style>
  :root {
    --backdrop: #e9e7e3;
    --card: #ffffff;
    --brand-blue: #1f4f9d;
    --rule-grey: #8d8f93;
    --tagline-grey: #555555;
    --ink: #111111;
    --body-ink: #222222;
  }
  html, body {
    margin: 0;
    padding: 0;
    width: 1200px;
    height: 1000px;
    overflow: hidden;
    background: var(--backdrop);
  }
  .canvas {
    position: relative;
    width: 1200px;
    height: 1000px;
  }
  .business-card {
    position: absolute;
    left: 421px;
    top: 193px;
    width: 358px;
    height: 613px;
    background: var(--card);
    border-radius: 18px;
    box-shadow: 0 4px 14px rgba(0,0,0,0.18);
    text-align: center;
    font-family: "Arimo", Arial, sans-serif;
    color: var(--body-ink);
  }
  .brand {
    position: absolute;
    left: 0;
    right: 0;
    top: 62px;
  }
  .brand-name {
    margin: 0;
    font-family: "Marcellus SC", serif;
    font-weight: 400;
    font-size: 27px;
    line-height: 32px;
    color: var(--brand-blue);
    letter-spacing: 0.5px;
  }
  .brand-rule {
    display: block;
    margin: 10px auto 0;
  }
  .tagline {
    position: absolute;
    left: 0;
    right: 0;
    top: 206px;
    margin: 0;
    font-family: "Marcellus SC", serif;
    font-size: 15.5px;
    line-height: 23px;
    color: var(--tagline-grey);
    letter-spacing: 0.3px;
  }
  .advisor {
    position: absolute;
    left: 0;
    right: 0;
    top: 297px;
  }
  .advisor-name {
    margin: 0;
    font-size: 17px;
    font-weight: 400;
    line-height: 22px;
    color: var(--ink);
    letter-spacing: 0.3px;
  }
  .advisor-details {
    margin: 4px 0 0;
    font-size: 14px;
    line-height: 20px;
  }
  .contact {
    position: absolute;
    left: 0;
    right: 0;
    top: 434px;
    font-size: 14px;
    line-height: 19.5px;
  }
  .contact p { margin: 0; }
  .contact .phones { margin-top: 9px; }
  .contact .email { margin-top: 6px; }
</style>
</head>
<body>
<div class="canvas">
  <article class="business-card">
    <header class="brand">
      <h1 class="brand-name">Harborlight Wealth<br>Partners, LLC</h1>
      <svg class="brand-rule" width="300" height="4" viewBox="0 0 300 4" aria-hidden="true">
        <line x1="0" y1="2" x2="300" y2="2" stroke="var(--rule-grey)" stroke-width="1.5"/>
      </svg>
    </header>

    <p class="tagline">Shaping Your Working Savings<br>Into a Confident Retirement</p>

    <section class="advisor">
      <h2 class="advisor-name">NEIL OSGOOD</h2>
      <p class="advisor-details">MSF, CPA<br>Senior Wealth Advisor, Licensed Representative</p>
    </section>

    <section class="contact">
      <p class="address">2876 Meadowbrook Pkwy.<br>Suite K418, Cedar Harbor<br>NC 23019</p>
      <p class="phones">Phone: (555) 218-3960<br>Toll Free Fax: (555) 218-3961</p>
      <p class="email">Email: nosgood@harborlightwp.example</p>
    </section>
  </article>
</div>
</body>
</html>
```